SilverLedgerOak - Double Sided Business Card

We are looking for design options or our business cards. We are a Business Solutions and HR solutions Provider - the theme is business, for this card.

Our brand colours are represented within our logo.

Details needed to be put on the front of the business card are:

Employees name: [Sample Name]
Role: [Sample Role]

Address: Suite 4 - Level 3/48 Halloran Avenue Parramatta NSW 2150
M: 0000 000 000
P: 1300 847 213
F: 1300 847 286
E: sample@silverledgeroak.com.au
www.silverledgeroak.com.au
Updates

Reason: Hello, could we please increase our deadline by 5 days. Thanking you, Tess

Target Market(s)

Business Owners, also Candidates looking for Employment

Industry/Entity Type

Business

Contact Information for Business Card

Role: [Sample Role]

M: 0000 000 000
P: 1300 847 213
F: 1300 847 286

Font styles to use
Sans Serif

Colors
3276b5
3176b5
0455a3
85abd2
cfdeed
ffffff
000000
1b1b1b
757575

Requirements
Must have
• Details needed to be put on the front of the business card are:
• Employees name: [Sample Name]
• Role: [Sample Role]
• Address: Suite 4 - Level 3/48 Halloran Avenue Parramatta NSW 2150
• M: 0000 000 000
• P: 1300 847 213
• F: 1300 847 286
• E: sample@silverledgeroak.com.au
• www.silverledgeroak.com.au
Nice to have
• Simplicity, clean and professional.

```html
<!DOCTYPE html>
<html lang="en">
<head>
<meta charset="utf-8">
<title>SilverLedgerOak Business Card</title>
<link rel="stylesheet" href="https://fonts.googleapis.com/css2?family=Open+Sans:wght@400;600;700&display=swap">
<style>
  :root {
    --brand-blue: #3276b5;
    --brand-deep: #0455a3;
    --brand-soft: #85abd2;
    --card-black: #1b1b1b;
    --ink-white: #ffffff;
    --ink-grey: #757575;
    --stage: #4a4542;
  }
  * { box-sizing: border-box; margin: 0; padding: 0; }
  html, body { width: 1200px; height: 864px; overflow: hidden; }
  body {
    background: var(--stage);
    font-family: "Open Sans", sans-serif;
    position: relative;
  }
  .card {
    position: absolute;
    top: 282px;
    width: 530px;
    height: 300px;
    background: var(--card-black);
    box-shadow: 0 10px 28px rgba(0,0,0,0.45);
  }
  .card--back { left: 55px; }
  .card--front { left: 615px; }

  /* Back side */
  .back-wordmark {
    position: absolute;
    left: 0; right: 0; top: 110px;
    text-align: center;
    font-weight: 700;
    font-size: 40px;
    color: #8d8d8d;
    letter-spacing: 0.5px;
  }
  .back-web {
    position: absolute;
    left: 0; right: 0; bottom: 50px;
    text-align: center;
    font-size: 16px;
    color: var(--ink-grey);
  }

  /* Front side */
  .brand {
    position: absolute;
    left: 26px; top: 104px;
    width: 230px;
  }
  .brand-row { display: flex; align-items: center; gap: 8px; }
  .brand-square { width: 18px; height: 18px; background: var(--brand-blue); flex: none; }
  .brand-name {
    font-weight: 700;
    font-size: 25px;
    color: var(--ink-white);
    white-space: nowrap;
  }
  .brand-rule {
    margin-top: 6px;
    height: 1px;
    background: var(--ink-white);
  }
  .brand-tagline {
    margin-top: 4px;
    font-size: 8.4px;
    font-weight: 600;
    color: var(--ink-white);
    white-space: nowrap;
  }
  .divider {
    position: absolute;
    left: 272px; top: 22px;
    width: 1px; height: 256px;
    background: linear-gradient(to bottom, transparent, #8a8a8a 30%, #8a8a8a 70%, transparent);
  }
  .details {
    position: absolute;
    left: 290px; top: 40px;
    color: var(--ink-white);
    font-size: 13.5px;
    line-height: 1.25;
  }
  .person-name { color: var(--brand-blue); font-weight: 700; font-size: 14px; }
  .person-role { font-weight: 700; font-size: 14px; margin-bottom: 6px; }
  .address { margin-bottom: 10px; }
  .contact-list { list-style: none; }
  .contact-item { display: flex; align-items: center; gap: 8px; }
  .contact-icon { width: 11px; height: 11px; flex: none; fill: var(--brand-blue); }
  .contact-item--plain { padding-left: 19px; }
</style>
</head>
<body>
  <section class="card card--back" aria-label="Card back">
    <div class="back-wordmark">SilverLedgerOak</div>
    <div class="back-web">www.silverledgeroak.com.au</div>
  </section>

  <section class="card card--front" aria-label="Card front">
    <div class="brand">
      <div class="brand-row">
        <span class="brand-square"></span>
        <span class="brand-name">SilverLedgerOak</span>
      </div>
      <div class="brand-rule"></div>
      <div class="brand-tagline">Helping small to medium business realise their potential</div>
    </div>

    <div class="divider"></div>

    <div class="details">
      <div class="person-name">LIAM HARPER</div>
      <div class="person-role">CEO/FOUNDER</div>
      <div class="address">Suite 4 - Level 3/48<br>Halloran Avenue<br>Parramatta NSW 2150</div>
      <ul class="contact-list">
        <li class="contact-item">
          <svg class="contact-icon" viewBox="0 0 12 12" aria-hidden="true"><path d="M1 3c0-1 1-2 2-2h6c1 0 2 1 2 2v1H8V3H4v1H1zM2 5h8l1 6H1z"/></svg>
          <span>1300 847 213</span>
        </li>
        <li class="contact-item">
          <svg class="contact-icon" viewBox="0 0 12 12" aria-hidden="true"><path d="M3 0h6v12H3zM4 1.5v8h4v-8z"/></svg>
          <span>0000 000 000</span>
        </li>
        <li class="contact-item">
          <svg class="contact-icon" viewBox="0 0 12 12" aria-hidden="true"><path d="M3 0h5v4H3zM1 4h10v7H1z"/></svg>
          <span>1300 847 286</span>
        </li>
        <li class="contact-item">
          <svg class="contact-icon" viewBox="0 0 12 12" aria-hidden="true"><circle cx="6" cy="6" r="5.5"/></svg>
          <span>sample@silverledgeroak.com.au</span>
        </li>
        <li class="contact-item contact-item--plain">
          <span>www.silverledgeroak.com.au</span>
        </li>
      </ul>
    </div>
  </section>
</body>
</html>
```